依頼詳細
堅苦しい会議等でもしっかりとした企業性を出しつつも、モダンでオシャレさインパクトも出せると最高にうれしく思います。
型押し等のオプション付きも可能ですが、型押しをなくした場合でも格好がいいものを希望します。
ベースカラーは白でお願いいたします。
モノクロでも使用できるようにお願いいたします。
記載項目
表面:会社名・ロゴ・役職名・名前・住所・電話番号・FAX番号・名前のローマ字表記
希望イメージ
シンプル 複雑
単色 カラフル
暗い 明るい
日常 高級
遊び心 厳粛
未来的 伝統的
女性的 男性的
希望する色
納品ファイル
• イラストレーター形式 (.ai)
補足説明
お世話になっております。

追記させていただきます。
名刺の向きを横型でお願いいたします。
初めに書いておけばよかったことですが・・・すみません。

裏面は、支店や店舗情報が3軒ほど乗せれればうれしく思います。
一応、既存の二店のロゴを添付しておきます。
ブラッシュアップしていただいても構いません。

裏面に店舗情報載せない場合の、イメージもあると大変うらしく思います。
よろしくお願いいたします。
■ 選んだ理由

ご提案いただきありがとうございました。
シンプルの中におしゃれさと、モダンさ、厳粛さが表現できているように思えたので、こちらを選ばさせていただきました。

ありがとうございました。

■ 提案者全員のお礼・コメント

たくさんのご提案をいただきまして、大変ありがとうございました。

また、追加依頼などあると思いますので、機会がありましたらまたよろしくお願いいたします。

```html
<!DOCTYPE html>
<html lang="ja">
<head>
<meta charset="utf-8">
<title>楓乃屋 名刺</title>
<link rel="stylesheet" href="https://fonts.googleapis.com/css2?family=Noto+Sans+JP:wght@400;500;700&family=Noto+Serif+JP:wght@500;700&display=swap">
<style>
  :root {
    --bg: #ececec;
    --card: #ffffff;
    --accent: #a3224a;
    --ink: #2b2b2b;
    --muted: #666666;
    --rule: #d9d9d9;
  }
  * { margin: 0; padding: 0; box-sizing: border-box; }
  html, body { width: 900px; height: 1200px; overflow: hidden; }
  body {
    background: var(--bg);
    font-family: "Noto Sans JP", sans-serif;
    color: var(--ink);
    position: relative;
  }
  .card {
    position: absolute;
    left: 60px;
    width: 780px;
    height: 510px;
    background: var(--card);
    box-shadow: 0 3px 12px rgba(0,0,0,0.15);
  }
  .card--front { top: 28px; }
  .card--back { top: 600px; }

  /* Front */
  .brand {
    position: absolute;
    top: 70px; left: 0; right: 0;
    text-align: center;
  }
  .brand__mark {
    display: block;
    width: 46px; height: 46px;
    margin: 0 auto 26px;
    border-radius: 50%;
    background: var(--accent);
  }
  .brand__name {
    font-family: "Noto Serif JP", serif;
    font-weight: 500;
    font-size: 40px;
    letter-spacing: 4px;
    color: var(--accent);
    line-height: 1;
  }
  .brand__kana {
    font-family: "Noto Serif JP", serif;
    font-weight: 500;
    font-size: 13px;
    color: var(--accent);
    margin-top: 8px;
    letter-spacing: 2px;
  }
  .person {
    position: absolute;
    top: 290px; left: 0; right: 0;
    text-align: center;
  }
  .person__title { font-size: 15px; letter-spacing: 2px; }
  .person__name {
    font-family: "Noto Serif JP", serif;
    font-weight: 500;
    font-size: 36px;
    letter-spacing: 14px;
    margin-top: 2px;
    line-height: 1.25;
  }
  .person__roman { font-size: 13px; letter-spacing: 5px; color: var(--muted); margin-top: 2px; }
  .company {
    position: absolute;
    top: 412px; left: 50px;
    font-size: 17px; font-weight: 500;
  }
  .divider {
    position: absolute;
    top: 446px; left: 50px; right: 50px;
    height: 1px; background: var(--rule);
  }
  .contact {
    position: absolute;
    left: 50px; right: 50px;
    font-size: 13px;
    display: flex; justify-content: space-between; align-items: center;
    color: var(--ink);
  }
  .contact--row1 { top: 458px; }
  .contact--row2 { top: 480px; }
  .contact__item { display: inline-flex; align-items: center; gap: 6px; }
  .contact__item + .contact__item { margin-left: 20px; }
  .contact__icon { width: 14px; height: 14px; fill: var(--muted); }

  /* Back */
  .shop {
    position: absolute;
    left: 60px; right: 50px;
    height: 120px;
    display: flex; align-items: center;
  }
  .shop--1 { top: 50px; }
  .shop--2 { top: 195px; }
  .shop--3 { top: 340px; }
  .shop__mark {
    width: 220px;
    display: flex; align-items: center; justify-content: center; gap: 10px;
  }
  .shop__dot { width: 16px; height: 16px; border-radius: 50%; background: var(--accent); }
  .shop__logotype {
    font-family: "Noto Serif JP", serif;
    font-weight: 700;
    font-size: 22px;
    color: var(--accent);
    letter-spacing: 1px;
  }
  .shop__bar {
    width: 4px; height: 100px;
    background: var(--accent);
    margin: 0 30px 0 20px;
  }
  .shop__info { font-size: 14px; line-height: 1.75; }
  .shop__name { font-weight: 700; font-size: 15px; margin-bottom: 6px; }
</style>
</head>
<body>
  <section class="card card--front">
    <div class="brand">
      <span class="brand__mark"></span>
      <div class="brand__name">KAEDEYA</div>
      <div class="brand__kana">楓乃屋</div>
    </div>
    <div class="person">
      <div class="person__title">代表取締役</div>
      <div class="person__name">佐藤 一郎</div>
      <div class="person__roman">SATO ICHIRO</div>
    </div>
    <div class="company">楓乃屋コーポレーション株式会社</div>
    <div class="divider"></div>
    <div class="contact contact--row1">
      <div><span class="contact__item">TEL 03-5550-2741</span><span class="contact__item">FAX 03-5550-2742</span></div>
      <span class="contact__item">
        <svg class="contact__icon" viewBox="0 0 16 16"><path d="M1 3h14v10H1z M2 4l6 5 6-5" fill="none" stroke="#666" stroke-width="1.4"/></svg>
        info-sato@kaedeya.example
      </span>
    </div>
    <div class="contact contact--row2">
      <span class="contact__item">〒870-0000 大分県架空市楓町2-14-7</span>
      <span class="contact__item">
        <svg class="contact__icon" viewBox="0 0 16 16"><rect x="4" y="1" width="8" height="14" rx="1.5" fill="none" stroke="#666" stroke-width="1.4"/><circle cx="8" cy="12.5" r="0.9"/></svg>
        090-5550-3318
      </span>
    </div>
  </section>

  <section class="card card--back">
    <div class="shop shop--1">
      <div class="shop__mark"><span class="shop__logotype">ささめ</span></div>
      <div class="shop__bar"></div>
      <div class="shop__info">
        <div class="shop__name">ささめカラオケダイニング</div>
        <div>〒870-0000 大分県架空市楓町2-14-7</div>
        <div>TEL 000-555-0192</div>
      </div>
    </div>
    <div class="shop shop--2">
      <div class="shop__mark"><span class="shop__logotype">SUZUNA</span><span class="shop__dot"></span></div>
      <div class="shop__bar"></div>
      <div class="shop__info">
        <div class="shop__name">SUZUNAそば道場</div>
        <div>〒870-0000 大分県架空市楓町2-14-7</div>
        <div>TEL 000-555-0192</div>
      </div>
    </div>
    <div class="shop shop--3">
      <div class="shop__mark"><span class="shop__dot"></span><span class="shop__logotype">KAEDEYA</span></div>
      <div class="shop__bar"></div>
      <div class="shop__info">
        <div class="shop__name">楓乃屋KAEDEYA</div>
        <div>〒870-0000 大分県架空市楓町2-14-7</div>
        <div>TEL 000-555-0192</div>
      </div>
    </div>
  </section>
</body>
</html>
```